Recycling Poster

HI
Looking for clean and clear new recycling posters for plastic bottles, glass bottles , and aluminium cans we have attached an industry sample we are looking for a new clean look and feel
Colour scheme light blue , yellow and font in black
size a2

Target Market(s)

consumer

Industry/Entity Type

Industry

Font styles to use
Sans Serif

Colors
fbee3e
33a6d7
acd036
faa54b

Requirements
Must have
• the logo *quillora I have just attached
Should not have
• do not include the "do the right thing text or tidy horizon logo and bin
• do not use crushed containers

```html
<!DOCTYPE html>
<html lang="en">
<head>
<meta charset="utf-8">
<title>Recycle Here Poster</title>
<link rel="stylesheet" href="https://fonts.googleapis.com/css2?family=Montserrat:wght@700;800;900&family=Anton&display=swap">
<style>
  :root {
    --sky: #33a6d7;
    --sky-light: #7fd0f2;
    --sky-deep: #1466b0;
    --navy: #0d4f94;
    --sun: #fbee3e;
    --leaf: #acd036;
    --leaf-deep: #3aa843;
    --ink: #111111;
    --paper: #ffffff;
    --orange: #faa54b;
    --alert: #e02020;
  }
  * { margin: 0; padding: 0; box-sizing: border-box; }
  html, body { width: 849px; height: 1200px; overflow: hidden; background: var(--paper); }
  .poster {
    position: relative;
    width: 849px; height: 1200px; overflow: hidden;
    background: radial-gradient(ellipse at 50% 40%, var(--sky-light) 0%, var(--sky) 45%, var(--sky-deep) 100%);
    font-family: "Montserrat", sans-serif;
  }
  .rays { position: absolute; inset: 0; }
  .containers-photo {
    position: absolute; left: 40px; top: 0; width: 770px; height: 330px;
    border-radius: 0 0 120px 120px;
    background: linear-gradient(180deg, #e9eef2 0%, #c9d4dc 55%, rgba(201,212,220,0) 100%);
    opacity: .85;
  }
  .target { position: absolute; left: 142px; top: 212px; width: 566px; height: 566px; }
  .headline {
    position: absolute; left: 205px; top: 385px; width: 440px;
    font-family: "Anton", sans-serif; font-weight: 400; font-size: 100px; line-height: 1.05;
    color: var(--ink); text-align: center; transform: rotate(10deg);
    letter-spacing: 2px;
  }
  .stage { position: absolute; left: -40px; top: 745px; width: 929px; height: 60px; }
  .materials {
    position: absolute; left: 0; top: 800px; width: 849px; height: 106px;
    display: flex; flex-direction: column; justify-content: center;
    background: rgba(13, 79, 148, .35);
    text-align: center; color: var(--paper);
    font-weight: 900; font-size: 32px; line-height: 1.25; letter-spacing: 1px;
  }
  .rule { position: absolute; left: 0; width: 849px; height: 4px; background: var(--sun); top: 906px; }
  .notice {
    position: absolute; left: 22px; width: 330px; height: 100px;
    display: flex; align-items: center; gap: 14px;
  }
  .notice--food { top: 930px; }
  .notice--bag { top: 1050px; }
  .notice__sign { width: 92px; height: 92px; flex: none; }
  .notice__label {
    background: var(--sun); color: var(--ink); font-weight: 800;
    font-size: 27px; line-height: 1.15; padding: 10px 16px; border-radius: 8px;
  }
  .brand-card {
    position: absolute; left: 384px; top: 962px; width: 438px; height: 140px;
    background: var(--paper); border: 6px solid var(--leaf-deep); border-radius: 22px;
    display: flex; align-items: center; justify-content: center; gap: 22px;
  }
  .brand-card__dot { width: 70px; height: 70px; border-radius: 50%; background: var(--leaf-deep); }
  .brand-card__name { font-weight: 900; font-size: 66px; color: var(--leaf-deep); letter-spacing: -1px; }
</style>
</head>
<body>
<main class="poster">
  <svg class="rays" viewBox="0 0 849 1200" aria-hidden="true">
    <g fill="#ffffff" opacity="0.12">
      <polygon points="425,495 0,60 0,260"/>
      <polygon points="425,495 0,420 0,600"/>
      <polygon points="425,495 849,60 849,260"/>
      <polygon points="425,495 849,420 849,600"/>
      <polygon points="425,495 120,0 300,0"/>
      <polygon points="425,495 560,0 740,0"/>
    </g>
  </svg>

  <div class="containers-photo" role="img" aria-label="Photo of clear plastic bottles, glass bottles and aluminium cans standing behind the sign"></div>

  <svg class="target" viewBox="0 0 566 566" aria-hidden="true">
    <circle cx="283" cy="283" r="283" fill="var(--sun)"/>
    <circle cx="283" cy="283" r="258" fill="var(--leaf)"/>
    <circle cx="283" cy="283" r="236" fill="var(--sun)"/>
    <circle cx="283" cy="283" r="214" fill="var(--paper)"/>
    <circle cx="283" cy="283" r="160" fill="#e7f2d6"/>
  </svg>
  <h1 class="headline">RECYCLE<br>HERE!</h1>

  <svg class="stage" viewBox="0 0 929 60" preserveAspectRatio="none" aria-hidden="true">
    <ellipse cx="464" cy="40" rx="470" ry="40" fill="#dff3fb"/>
  </svg>

  <p class="materials">
    <span>PLASTIC BOTTLES • GLASS BOTTLES</span>
    <span>ALUMINIUM CANS</span>
  </p>
  <div class="rule"></div>

  <div class="notice notice--food">
    <svg class="notice__sign" viewBox="0 0 100 100" role="img" aria-label="No food scraps sign">
      <rect x="4" y="4" width="92" height="92" rx="10" fill="var(--sun)"/>
      <rect x="28" y="38" width="44" height="30" rx="6" fill="var(--orange)"/>
      <circle cx="50" cy="50" r="36" fill="none" stroke="var(--alert)" stroke-width="7"/>
      <line x1="25" y1="75" x2="75" y2="25" stroke="var(--alert)" stroke-width="7"/>
    </svg>
    <span class="notice__label">No Food<br>Scraps</span>
  </div>

  <div class="notice notice--bag">
    <svg class="notice__sign" viewBox="0 0 100 100" role="img" aria-label="No plastic bag sign">
      <rect x="4" y="4" width="92" height="92" rx="10" fill="var(--sun)"/>
      <rect x="32" y="36" width="36" height="38" rx="4" fill="#c9b98a"/>
      <circle cx="50" cy="50" r="36" fill="none" stroke="var(--alert)" stroke-width="7"/>
      <line x1="25" y1="75" x2="75" y2="25" stroke="var(--alert)" stroke-width="7"/>
    </svg>
    <span class="notice__label">No Plastic<br>Bag</span>
  </div>

  <div class="brand-card">
    <span class="brand-card__dot"></span>
    <span class="brand-card__name">quillora</span>
  </div>
</main>
</body>
</html>
```